BRISK Study flyer

I need help designing a flyer for a research study that will include brain imaging in adolescents. The info is in the attached document. The study is called the Brain Rhythms In School Kids (BRISK) study. Ideally this would be returned as a document that I can edit in the future as we will have several new recruitment phases (different age groups, etc. I also would love to have a logo designed as part of this project, but I recognize that might be a separate design request.

```html
<!DOCTYPE html>
<html lang="en">
<head>
<meta charset="utf-8">
<title>BRISK Study Flyer</title>
<link rel="stylesheet" href="https://fonts.googleapis.com/css2?family=Poppins:wght@300;400;500;600;700;800&family=Oswald:wght@500;700&display=swap">
<style>
  :root {
    --navy: #1b2657;
    --navy-text: #1d2a5c;
    --green: #3db54a;
    --orange: #f7901e;
    --yellow: #fcd14d;
    --pink: #e8a2b2;
    --lilac: #c5a9d3;
    --paper-top: #e9e9eb;
    --paper-bottom: #ffffff;
    --stage: #e2e2e4;
    --white: #ffffff;
  }
  * { margin: 0; padding: 0; box-sizing: border-box; }
  html, body { width: 1200px; height: 2182px; overflow: hidden; }
  body {
    background: var(--stage);
    font-family: "Poppins", sans-serif;
    position: relative;
  }
  .flyer {
    position: absolute;
    left: 40px; top: 299px;
    width: 1120px; height: 1584px;
    overflow: hidden;
    background: linear-gradient(180deg, var(--paper-top) 0%, var(--paper-bottom) 70%);
    box-shadow: 0 4px 18px rgba(0,0,0,.15);
  }
  .backdrop { position: absolute; inset: 0; }
  .hero-art {
    position: absolute;
    left: 560px; top: 0; width: 560px; height: 600px;
    background: linear-gradient(180deg, rgba(252,209,77,.35) 0%, rgba(252,209,77,.85) 45%, #d8c47a 100%);
    border-radius: 0 0 0 40px;
  }
  .intro-frame {
    position: absolute;
    left: 59px; top: 349px; width: 484px; height: 1118px;
    border-radius: 90px 0 0 90px;
    background: rgba(255,255,255,.55);
  }
  .intro-panel {
    position: absolute;
    left: 71px; top: 365px; width: 467px; height: 1098px;
    border-radius: 82px 0 0 82px;
    background: var(--navy);
    color: var(--white);
    padding: 70px 30px 0 47px;
  }
  .headline {
    font-weight: 800;
    font-size: 56px;
    line-height: 75px;
    letter-spacing: -0.5px;
  }
  .headline .green { color: var(--green); }
  .headline .orange { color: var(--orange); }
  .headline .yellow { color: var(--yellow); }
  .question {
    margin-top: 52px;
    font-weight: 300;
    font-size: 32px;
    line-height: 45px;
    text-transform: uppercase;
  }
  .summary {
    margin-top: 46px;
    max-width: 350px;
    font-weight: 300;
    font-size: 22px;
    line-height: 30px;
  }
  .panel-art {
    position: absolute;
    left: 72px; bottom: 0; width: 394px; height: 247px;
    border-radius: 40px 40px 0 0;
    background: linear-gradient(160deg, #2d3a72 0%, #4a3f80 55%, #c16d8a 100%);
    opacity: .75;
  }
  .details-frame {
    position: absolute;
    left: 608px; top: 709px; width: 459px; height: 695px;
    border: 5px solid var(--green);
    border-left: none;
    border-radius: 0 36px 36px 0;
  }
  .details {
    position: absolute;
    left: 581px; top: 748px; width: 450px;
    color: var(--navy-text);
  }
  .details h2 {
    font-weight: 700;
    font-size: 26px;
    line-height: 30px;
    text-transform: uppercase;
  }
  .details .involves { white-space: nowrap; }
  .details ul {
    list-style: none;
    margin-top: 12px;
  }
  .details li {
    position: relative;
    padding-left: 38px;
    font-size: 21px;
    line-height: 25px;
    margin-bottom: 15px;
  }
  .details li::before {
    content: "";
    position: absolute;
    left: 20px; top: 11px;
    width: 5px; height: 5px; border-radius: 50%;
    background: var(--navy-text);
  }
  .details .eligibility { margin-top: 46px; }
  .badge {
    position: absolute;
    left: 880px; top: 1355px; width: 216px; height: 216px;
  }
  .badge-text {
    position: absolute;
    inset: 0;
    display: flex; flex-direction: column; align-items: center; justify-content: center;
    transform: rotate(-8deg);
    font-family: "Oswald", sans-serif;
    color: var(--navy);
    text-align: center;
    padding-top: 6px;
  }
  .badge-text .label { font-weight: 500; font-size: 24px; line-height: 26px; }
  .badge-text .sub { font-weight: 500; font-size: 20px; line-height: 26px; }
  .badge-text .amount {
    font-family: "Poppins", sans-serif;
    font-weight: 800; font-size: 62px; line-height: 62px; letter-spacing: -1px;
  }
  .contact {
    position: absolute;
    left: 118px; top: 1480px;
    color: var(--navy-text);
  }
  .contact .prompt {
    color: var(--green);
    font-weight: 700;
    font-size: 26px;
    line-height: 36px;
  }
  .contact .line {
    margin-top: 12px;
    font-size: 20px;
    line-height: 32px;
  }
  .contact .email {
    font-weight: 700;
    font-size: 27px;
  }
</style>
</head>
<body>
  <main class="flyer">
    <svg class="backdrop" width="1120" height="1584" viewBox="0 0 1120 1584" aria-hidden="true">
      <ellipse cx="705" cy="350" rx="345" ry="390" fill="var(--pink)" opacity=".55"/>
      <ellipse cx="860" cy="330" rx="300" ry="330" fill="var(--pink)" opacity=".45"/>
      <ellipse cx="960" cy="420" rx="260" ry="300" fill="var(--lilac)" opacity=".5"/>
    </svg>

    <div class="hero-art" role="img" aria-label="Photo collage: a hanging lamp shining a yellow spotlight on a girl writing on a stack of books"></div>

    <div class="intro-frame"></div>
    <section class="intro-panel">
      <h1 class="headline">
        <span class="green">ARE YOU THE</span><br>
        <span class="orange">PARENT OF A</span><br>
        <span class="orange">CHILD AGE</span><br>
        <span class="yellow">10-17?</span>
      </h1>
      <p class="question">Do they worry or overthink negative emotions?</p>
      <p class="summary">Lakeview University researchers are seeking girls age 10-17 for a study about brain activity in emotions and decision-making and how they relate to puberty, anxiety and depression.</p>
      <div class="panel-art" role="img" aria-label="Illustration of a student reading on a pile of books surrounded by school icons"></div>
    </section>

    <div class="details-frame"></div>
    <section class="details">
      <h2 class="involves">Study participation involves:</h2>
      <ul>
        <li>One one-hour interview (online or in-person) where your child will discuss their thoughts</li>
        <li>Online questionnaires (parent and child)</li>
        <li>One two-hour visit where your child will complete an MRI scan, answer questions about their puberty stage, and have a small hair sample taken to study puberty hormones</li>
      </ul>
      <h2 class="eligibility">Your child may be eligible if<br>they:</h2>
      <ul>
        <li>Are age 10-17</li>
        <li>Tend to worry or overthink negative thoughts</li>
        <li>have not been diagnosed with psychosis, learning problems, or autism</li>
      </ul>
    </section>

    <div class="badge">
      <svg width="216" height="216" viewBox="0 0 216 216" aria-hidden="true">
        <circle cx="108" cy="108" r="92" fill="var(--green)"/>
        <circle cx="108" cy="108" r="98" fill="none" stroke="var(--green)" stroke-width="16" stroke-dasharray="9 7"/>
      </svg>
      <div class="badge-text">
        <span class="label">COMPENSATION</span>
        <span class="sub">UP TO</span>
        <span class="amount">$140</span>
      </div>
    </div>

    <footer class="contact">
      <p class="prompt">Interested in participating?&nbsp; Want more information?</p>
      <p class="line">Please contact us! <span class="email">briskstudy@lakeview.edu</span></p>
    </footer>
  </main>
</body>
</html>
```